Harlow Stonefield Civil Construction website design

We want a Bold website to promote our Heavy Civil Construction company, We would like an organic / tangible feel to the site. The pictures will be over saturated so they pop. We need to be able to easliy upload new projects and pictures on a regular basis.
Home page will have a full screen width image, "home page image" with silhouette and logo. It will also have about us area and picture
Page 2 will be Project Gallery with pictures in project folders
Page 3 will be an employment application form and submission
Page 4 will be Contact Us
Target Market(s)
Construction indusrty
Industry/Entity Type
Contractor
Coding
Coded - Design and coding required
Number of Pages Required
4 page
Font styles to use
Other font styles liked:
- Hypatia Sans Pro Light
Look and feel

```html
<!DOCTYPE html>
<html lang="en">
<head>
<meta charset="utf-8">
<title>Harlow Stonefield Civil Construction</title>
<link href="https://fonts.googleapis.com/css2?family=Montserrat:wght@400;500;600;700&display=swap" rel="stylesheet">
<style>
:root{
  --ink:#2b2b2b;
  --muted:#8a8a8a;
  --brand:#2e3f96;
  --gold:#e6c23c;
  --white:#ffffff;
  --footer:#1c1c1c;
  --navy:#1d2a4f;
}
*{margin:0;padding:0;box-sizing:border-box}
html,body{width:694px;height:1200px;overflow:hidden;background:var(--white)}
body{position:relative;font-family:'Montserrat',sans-serif;color:var(--ink)}
.abs{position:absolute}

.brand{left:23px;top:36px;display:flex;align-items:center;gap:5px}
.brand-square{width:20px;height:22px;border:2px solid var(--brand)}
.brand-name{color:var(--brand);font-weight:500;font-size:8.6px;line-height:10px;letter-spacing:.3px;border-left:1px solid var(--brand);padding-left:4px}
.brand-name span{display:block;font-size:5.4px;letter-spacing:1.6px;line-height:8px}

.nav a{position:absolute;top:45px;font-size:8px;font-weight:500;color:var(--ink);text-decoration:none;letter-spacing:.2px}
.nav a.is-home{color:var(--muted)}
.nav .underline{position:absolute;left:505px;top:56px;width:42px;height:1px;background:var(--gold)}

.hero{left:21px;top:100px;width:651px;height:261px;background:linear-gradient(160deg,#3d6b33 0%,#9a9a86 35%,#5f8a3e 60%,#2f5a2a 100%)}
.dots span{position:absolute;top:111px;height:1.3px;width:30px;background:var(--white)}
.dots span.active{background:var(--gold)}
.hero-arrow{top:224px}
.caption-scope{left:130px;top:317px;width:130px;height:44px;background:var(--white)}
.caption-project{left:260px;top:317px;width:304px;height:44px;background:var(--gold)}
.cap-title{font-size:7px;font-weight:600;letter-spacing:.4px;color:var(--ink)}
.cap-label{font-size:6px;letter-spacing:.5px;color:var(--muted);margin-top:4px}
.caption-project .cap-title,.caption-project .cap-label{color:#5a4a10}
.cap-item{position:absolute;top:13px}

.photo{position:absolute}
.about-title{left:274px;top:448px;font-size:16px;font-weight:700;letter-spacing:1px}
.about-rule{left:275px;top:473px;width:22px;height:1.5px;background:var(--gold)}
.about-text{left:274px;width:390px;font-size:7.6px;line-height:15.7px;letter-spacing:.25px;text-align:justify;text-align-last:left}

.card{position:absolute;top:833px;width:208px;height:151px}
.card-label{position:absolute;top:998px;width:208px;text-align:center;font-size:7.5px;font-weight:600;letter-spacing:.8px}
.card-copy{position:absolute;left:16px;right:10px;top:22px;color:var(--white);font-size:6.3px;line-height:15.7px;letter-spacing:.3px;text-align:justify}

.footer{left:0;top:1091px;width:694px;height:109px;background:var(--footer);color:var(--white)}
.footer a{position:absolute;top:47px;font-size:8px;font-weight:500;color:var(--white);text-decoration:none}
.footer a.is-current{color:var(--gold)}
.follow{position:absolute;left:510px;top:46px;font-size:8px;font-weight:500}
.social{position:absolute;top:46px;width:11px;height:11px;background:var(--white)}
.social.is-current{background:var(--gold)}
.footer-rule{position:absolute;left:21px;top:91px;width:651px;height:1px;background:#cfcfcf}
.legal{position:absolute;top:96px;font-size:5.3px;font-weight:600;color:#d8d8d8}
</style>
</head>
<body>

<header>
  <div class="abs brand">
    <div class="brand-square"></div>
    <div class="brand-name">HARLOW STONEFIELD<span>CIVIL CONSTRUCTION</span></div>
  </div>
  <nav class="nav">
    <a class="is-home" style="left:393px">HOME</a>
    <a style="left:442px">SERVICES</a>
    <a style="left:505px">PROJECTS</a>
    <a style="left:571px">CAREERS</a>
    <a style="left:633px">CONTACT</a>
    <div class="underline"></div>
  </nav>
</header>

<section>
  <div class="abs hero" role="img" aria-label="Aerial photo of a land development site with trees, a lake and houses"></div>
  <div class="dots">
    <span style="left:251px"></span><span class="active" style="left:290px"></span><span style="left:329px"></span><span style="left:368px"></span><span style="left:407px"></span>
  </div>
  <svg class="abs hero-arrow" style="left:31px" width="10" height="14" viewBox="0 0 10 14"><path d="M7 1 L2 7 L7 13" fill="none" stroke="#fff" stroke-width="1.2"/></svg>
  <svg class="abs hero-arrow" style="left:653px" width="10" height="14" viewBox="0 0 10 14"><path d="M3 1 L8 7 L3 13" fill="none" stroke="#fff" stroke-width="1.2"/></svg>
  <div class="abs caption-scope">
    <div class="cap-item" style="left:13px"><div class="cap-title">LAND DEVELOPMENT</div><div class="cap-label">SCOPE</div></div>
  </div>
  <div class="abs caption-project">
    <div class="cap-item" style="left:13px"><div class="cap-title">CEDAR HOLLOW DISTRICT PARK</div><div class="cap-label">PROJECT NAME</div></div>
    <div class="cap-item" style="left:178px"><div class="cap-title">TAMPA, FL</div><div class="cap-label">LOCATION</div></div>
    <svg class="abs" style="left:285px;top:18px" width="10" height="8" viewBox="0 0 10 8"><path d="M0 4 H9 M6 1 L9 4 L6 7" fill="none" stroke="#5a4a10" stroke-width="0.9"/></svg>
  </div>
</section>

<section>
  <div class="photo" style="left:21px;top:449px;width:113px;height:90px;background:linear-gradient(180deg,#3f6a35 0%,#8c8f86 45%,#3f4a42 75%,#a3a39b 100%)" role="img" aria-label="Rock-lined drainage channel"></div>
  <div class="photo" style="left:148px;top:449px;width:112px;height:90px;background:linear-gradient(135deg,#4e6a3a 0%,#9a8c74 50%,#3d4d33 100%)" role="img" aria-label="Aerial view of a construction site with equipment"></div>
  <div class="photo" style="left:21px;top:553px;width:240px;height:97px;background:linear-gradient(180deg,#c7d2de 0%,#e3e8ee 35%,#3d5c3a 50%,#6ec3a4 70%,#5c8e80 90%)" role="img" aria-label="Retention pond with hydroseeded banks"></div>
  <div class="photo" style="left:21px;top:664px;width:113px;height:90px;background:linear-gradient(160deg,#8b7a62 0%,#b5ada0 45%,#6e5a44 100%)" role="img" aria-label="Concrete drainage structure being installed"></div>
  <div class="photo" style="left:148px;top:663px;width:112px;height:91px;background:linear-gradient(160deg,#3b4a35 0%,#9b8e7c 40%,#cfc9bf 65%,#a69784 100%)" role="img" aria-label="New concrete curb along a graded road"></div>

  <h2 class="abs about-title">ABOUT US</h2>
  <div class="abs about-rule"></div>
  <p class="abs about-text" style="top:491px">Lorem ipsum dolor sit amet, consectetur adipiscing elit, sed do eiusmod tempor incididunt ut labore et dolore magna aliqua. Quis ipsum suspendisse ultrices gravida. Risus commodo viverra maecenas accumsan lacus vel facilisis.</p>
  <p class="abs about-text" style="top:554px">Lorem ipsum dolor sit amet, consectetur adipiscing elit, sed do eiusmod tempor incididunt ut labore et dolore magna aliqua. Quis ipsum suspendisse ultrices gravida. Risus commodo viverra maecenas accumsan lacus vel facilisis. Quis ipsum suspendisse ultrices gravida. Risus commodo viverra maecenas accumsan lacus vel facilisis. Quis ipsum suspendisse ultrices gravida. Risus commodo viverra maecenas accumsan lacus vel facilisis.</p>
  <p class="abs about-text" style="top:648px">Lorem ipsum dolor sit amet, consectetur adipiscing elit, sed do eiusmod tempor incididunt ut labore et dolore magna aliqua. Quis ipsum suspendisse ultrices gravida. Risus commodo viverra maecenas accumsan lacus vel facilisis.</p>
  <p class="abs about-text" style="top:710px">Lorem ipsum dolor sit amet, consectetur adipiscing elit, sed do eiusmod tempor incididunt ut labore et dolore magna aliqua. Quis ipsum suspendisse ultrices gravida. Risus commodo viverra maecenas accumsan lacus vel facilisis.</p>
</section>

<section>
  <div class="card" style="left:21px;background:linear-gradient(180deg,#b9c7d8 0%,#7e8c82 25%,#4f7a3d 50%,#6b5e3e 75%,#a49a80 100%)" role="img" aria-label="Aerial view of a lake beside a residential community"></div>
  <div class="card" style="left:243px;background:linear-gradient(180deg,#243358 0%,#1d2a4f 60%,#151f3a 100%)" role="img" aria-label="Dark blue tinted photo of a building with reflecting pool">
    <p class="card-copy">Lorem ipsum dolor sit amet, consectetur adipiscing elit, sed do eiusmod tempor incididunt ut labore et dolore magna aliqua. Quis ipsum suspendisse ultrices gravida. Risus commodo viverra maecenas accumsan lacus vel facilisis....</p>
  </div>
  <div class="card" style="left:464px;background:linear-gradient(180deg,#3a3a3c 0%,#5b5b5d 50%,#7a7a7a 100%)" role="img" aria-label="Open-plan office with people working at desks"></div>
  <div class="card-label" style="left:21px">PROJECTS</div>
  <div class="card-label" style="left:243px">SERVICES</div>
  <div class="card-label" style="left:464px">CONTACT</div>
</section>

<footer class="abs footer">
  <a style="left:23px">HOME</a>
  <a style="left:72px">CAREERS</a>
  <a class="is-current" style="left:134px">CONTACT</a>
  <div class="follow">FOLLOW US</div>
  <span class="social" style="left:582px"></span>
  <span class="social is-current" style="left:601px"></span>
  <span class="social" style="left:621px"></span>
  <span class="social" style="left:641px"></span>
  <span class="social" style="left:661px"></span>
  <div class="footer-rule"></div>
  <div class="legal" style="left:21px">@ HARLOW STONEFIELD Civil Construction 2019 All Rights Reserved</div>
  <div class="legal" style="right:22px">Privacy Policy | Terms &amp; Conditions</div>
</footer>

</body>
</html>
```